Hospital Digital Whiteboard UI/UX Redesign

We are looking to update the look and feel of our Digital Whiteboards.
There are 4 separate layouts: Patient TV, Patient Room Whiteboard, Digital Door Sign, and Unit Care Board.
We want to have a unified, modern look across the portfolio.

```html
<!DOCTYPE html>
<html lang="en">
<head>
<meta charset="utf-8">
<title>Digital Whiteboard – Door Sign and Unit Care Board</title>
<link href="https://fonts.googleapis.com/css2?family=Roboto:wght@300;400;500;700;900&display=swap" rel="stylesheet">
<style>
  :root {
    --page: #ffffff;
    --ink: #262626;
    --navy: #253750;
    --board-bg: #f2f4f7;
    --head-blue: #2a6fc0;
    --alert-blue: #4f52d0;
    --red: #c9372b;
    --orange: #ec8318;
    --yellow: #e0c014;
    --yellow-soft: #e2c04a;
    --green-dark: #317a3a;
    --teal: #31aa92;
    --slate-blue: #275a86;
    --pill-blue: #6ab1f7;
    --pill-green: #2bd60f;
    --code-blue: #0a7cf5;
    --emer-red: #ee3d3d;
    --pa-orange: #ea7d22;
  }
  * { box-sizing: border-box; margin: 0; padding: 0; }
  html, body { width: 1200px; height: 1035px; overflow: hidden; background: var(--page); }
  body { position: relative; font-family: "Roboto", sans-serif; color: var(--ink); }

  /* ---------- Door sign ---------- */
  .door-sign {
    position: absolute; left: 41px; top: 50px; width: 531px; height: 934px;
    background: #fff; box-shadow: 0 0 10px rgba(0,0,0,0.08);
  }
  .status-rail {
    position: absolute; left: 17px; top: 18px; width: 98px; height: 899px;
    background: #fff; box-shadow: 0 0 6px rgba(0,0,0,0.1); border-radius: 3px;
    padding: 8px 0 0 9px; display: flex; flex-direction: column; gap: 23px;
  }
  .status-tile {
    width: 81px; height: 90px; border-radius: 3px; color: #fff;
    display: flex; flex-direction: column; align-items: center; justify-content: center;
  }
  .status-tile .abbr { font-size: 44px; font-weight: 500; line-height: 1; letter-spacing: -1px; }
  .status-tile .label { font-size: 8px; font-weight: 700; margin-top: 4px; }
  .tile-red { background: var(--red); }
  .tile-orange { background: var(--orange); }
  .tile-yellow { background: var(--yellow); }
  .tile-green { background: var(--green-dark); }
  .tile-teal { background: var(--teal); }
  .tile-slate { background: var(--slate-blue); }

  .room-id {
    position: absolute; left: 117px; top: 0; width: 414px; height: 303px; text-align: center;
  }
  .room-id .caption { position: absolute; left: 0; right: 0; font-weight: 500; }
  .room-id .room-word { top: 54px; font-size: 26px; }
  .room-id .room-number { top: 92px; left: 0; right: 0; position: absolute; font-size: 118px; font-weight: 900; line-height: 1; letter-spacing: 2px; }
  .room-id .room-code { top: 222px; font-size: 25px; }

  .alert-panel {
    position: absolute; left: 117px; top: 303px; width: 414px; height: 631px; overflow: hidden;
    color: #fff; text-align: center;
  }
  .alert-backdrop {
    position: absolute; inset: 0;
    background: linear-gradient(160deg, #5356d6 0%, #4a4dcc 55%, #4346c0 100%);
  }
  .alert-text { position: absolute; left: 0; right: 0; line-height: 1; }
  .alert-code { top: 115px; font-size: 112px; font-weight: 900; letter-spacing: -2px; }
  .alert-blue { top: 252px; font-size: 112px; font-weight: 900; letter-spacing: -2px; }
  .alert-timer { top: 402px; font-size: 76px; font-weight: 300; }
  .alert-caption { top: 493px; font-size: 50px; font-weight: 300; }

  /* ---------- Unit care board ---------- */
  .care-board {
    position: absolute; left: 628px; top: 50px; width: 531px; height: 934px;
    background: var(--board-bg); box-shadow: 0 0 10px rgba(0,0,0,0.08);
  }
  .board-header {
    height: 35px; background: var(--navy); color: #fff; position: relative;
    display: flex; align-items: center; justify-content: center;
  }
  .board-title { font-size: 17px; font-weight: 500; }
  .board-clock { position: absolute; right: 16px; font-size: 9px; font-weight: 500; }

  .board-grid {
    display: grid;
    grid-template-columns: 28px 46px 40px 48px 42px 90px 90px 131px;
    align-items: center;
  }
  .column-heads {
    position: absolute; left: 8px; top: 53px; width: 515px; height: 14px;
    color: var(--head-blue); font-size: 8px; font-weight: 700; text-align: center;
  }
  .patient-list {
    position: absolute; left: 8px; top: 78px; width: 515px;
    display: flex; flex-direction: column; gap: 10.8px;
  }
  .patient-row {
    height: 34px; background: #fff; border-radius: 5px;
    box-shadow: 0 1px 3px rgba(0,0,0,0.08);
    font-size: 8px; text-align: center; color: #333;
  }
  .patient-row > span { display: flex; justify-content: center; align-items: center; }
  .pill {
    width: 67px; height: 19px; border-radius: 10px; color: #fff; font-weight: 500;
    display: flex; align-items: center; justify-content: center; font-size: 7.5px;
  }
  .pill-blue { background: var(--pill-blue); }
  .pill-green { background: var(--pill-green); }
  .plain-status { font-weight: 500; color: #222; }
  .alert-chip {
    width: 75px; height: 33px; border-radius: 3px; color: #fff; font-weight: 700; font-size: 7.5px;
    display: flex; align-items: center; justify-content: center;
  }
  .chip-code { background: var(--code-blue); }
  .chip-emer { background: var(--emer-red); }
  .plain-alert { font-weight: 700; color: #222; }
  .badges { justify-content: flex-start !important; gap: 2px; padding-left: 15px; }
  .badge {
    width: 26px; height: 26px; border-radius: 5px; color: #fff; font-size: 10px; font-weight: 500;
    display: flex; align-items: center; justify-content: center;
  }
  .b-cp, .b-ap { background: var(--red); }
  .b-fr { background: var(--yellow-soft); }
  .b-wc { background: var(--green-dark); }
  .b-np, .b-ns { background: var(--teal); }
  .b-pa { background: var(--pa-orange); }

  .pager { position: absolute; left: 0; right: 0; top: 895px; display: flex; justify-content: center; gap: 17px; }
</style>
</head>
<body>

<section class="door-sign">
  <div class="status-rail">
    <div class="status-tile tile-red"><span class="abbr">CP</span><span class="label">Lorem ipsum</span></div>
    <div class="status-tile tile-red"><span class="abbr">DP</span><span class="label">Lorem ipsum</span></div>
    <div class="status-tile tile-orange"><span class="abbr">LA</span><span class="label">Lorem ipsum</span></div>
    <div class="status-tile tile-yellow"><span class="abbr">FR</span><span class="label">Lorem ipsum</span></div>
    <div class="status-tile tile-green"><span class="abbr">EN</span><span class="label">Lorem ipsum</span></div>
    <div class="status-tile tile-teal"><span class="abbr">NS</span><span class="label">Lorem ipsum</span></div>
    <div class="status-tile tile-teal"><span class="abbr">NS</span><span class="label">Lorem ipsum</span></div>
    <div class="status-tile tile-slate"><span class="abbr">VE</span><span class="label">Lorem ipsum</span></div>
  </div>

  <div class="room-id">
    <div class="caption room-word">ROOM</div>
    <div class="room-number">216</div>
    <div class="caption room-code">GOR_S</div>
  </div>

  <div class="alert-panel">
    <div class="alert-backdrop" role="img" aria-label="Blue-tinted photo of a hospital room with a care team at a bedside"></div>
    <div class="alert-text alert-code">CODE</div>
    <div class="alert-text alert-blue">BLUE</div>
    <div class="alert-text alert-timer">02:24</div>
    <div class="alert-text alert-caption">ELAPSED TIME</div>
  </div>
</section>

<section class="care-board">
  <header class="board-header">
    <h1 class="board-title">Unit 2 West</h1>
    <span class="board-clock">1:00 PM</span>
  </header>

  <div class="column-heads board-grid">
    <span>RM</span><span>Lorem</span><span>Lorem</span><span>Lorem</span><span>Lorem</span><span>Lorem</span><span>Lorem</span><span>Lorem</span>
  </div>

  <div class="patient-list">
    <div class="patient-row board-grid"><span>201</span><span>K.M.</span><span>Lorem</span><span>Lorem</span><span>1:30 PM</span><span><i class="pill pill-blue">Doctor In Room</i></span><span><i class="alert-chip chip-code">CODE BLUE 00:35</i></span><span class="badges"><b class="badge b-cp">CP</b><b class="badge b-ap">AP</b><b class="badge b-fr">FR</b><b class="badge b-wc">WC</b></span></div>
    <div class="patient-row board-grid"><span>202</span><span>M.M.</span><span>Lorem</span><span>Lorem</span><span>1:30 PM</span><span class="plain-status">Vacant</span><span></span><span class="badges"><b class="badge b-np">NP</b><b class="badge b-ns">NS</b></span></div>
    <div class="patient-row board-grid"><span>202</span><span>M.M.</span><span>Lorem</span><span>Lorem</span><span>1:30 PM</span><span><i class="pill pill-blue">staff In Room</i></span><span><i class="alert-chip chip-emer">Staff Emer 00:35</i></span><span class="badges"><b class="badge b-fr">FR</b></span></div>
    <div class="patient-row board-grid"><span>202</span><span>M.M.</span><span>Lorem</span><span>Lorem</span><span>1:30 PM</span><span class="plain-status">Vacant</span><span></span><span class="badges"><b class="badge b-pa">PA</b></span></div>

    <div class="patient-row board-grid"><span>201</span><span>K.M.</span><span>Lorem</span><span>Lorem</span><span>1:30 PM</span><span><i class="pill pill-green">Doctor In Room</i></span><span class="plain-alert">Water 00:35</span><span class="badges"><b class="badge b-cp">CP</b><b class="badge b-ap">AP</b><b class="badge b-fr">FR</b><b class="badge b-wc">WC</b></span></div>
    <div class="patient-row board-grid"><span>202</span><span>M.M.</span><span>Lorem</span><span>Lorem</span><span>1:30 PM</span><span><i class="pill pill-green">Vacant</i></span><span></span><span class="badges"><b class="badge b-np">NP</b><b class="badge b-ns">NS</b></span></div>
    <div class="patient-row board-grid"><span>202</span><span>M.M.</span><span>Lorem</span><span>Lorem</span><span>1:30 PM</span><span><i class="pill pill-green">staff In Room</i></span><span><i class="alert-chip chip-emer">Staff Emer 00:35</i></span><span class="badges"><b class="badge b-fr">FR</b></span></div>
    <div class="patient-row board-grid"><span>202</span><span>M.M.</span><span>Lorem</span><span>Lorem</span><span>1:30 PM</span><span><i class="pill pill-blue">Vacant</i></span><span></span><span class="badges"><b class="badge b-pa">PA</b></span></div>

    <div class="patient-row board-grid"><span>201</span><span>K.M.</span><span>Lorem</span><span>Lorem</span><span>1:30 PM</span><span><i class="pill pill-green">Doctor In Room</i></span><span class="plain-alert">Water 00:35</span><span class="badges"><b class="badge b-cp">CP</b><b class="badge b-ap">AP</b><b class="badge b-fr">FR</b><b class="badge b-wc">WC</b></span></div>
    <div class="patient-row board-grid"><span>202</span><span>M.M.</span><span>Lorem</span><span>Lorem</span><span>1:30 PM</span><span><i class="pill pill-green">Vacant</i></span><span></span><span class="badges"><b class="badge b-np">NP</b><b class="badge b-ns">NS</b></span></div>
    <div class="patient-row board-grid"><span>202</span><span>M.M.</span><span>Lorem</span><span>Lorem</span><span>1:30 PM</span><span><i class="pill pill-green">staff In Room</i></span><span><i class="alert-chip chip-emer">Staff Emer 00:35</i></span><span class="badges"><b class="badge b-fr">FR</b></span></div>
    <div class="patient-row board-grid"><span>202</span><span>M.M.</span><span>Lorem</span><span>Lorem</span><span>1:30 PM</span><span><i class="pill pill-blue">Vacant</i></span><span></span><span class="badges"><b class="badge b-pa">PA</b></span></div>

    <div class="patient-row board-grid"><span>201</span><span>K.M.</span><span>Lorem</span><span>Lorem</span><span>1:30 PM</span><span><i class="pill pill-green">Doctor In Room</i></span><span class="plain-alert">Water 00:35</span><span class="badges"><b class="badge b-cp">CP</b><b class="badge b-ap">AP</b><b class="badge b-fr">FR</b><b class="badge b-wc">WC</b></span></div>
    <div class="patient-row board-grid"><span>202</span><span>M.M.</span><span>Lorem</span><span>Lorem</span><span>1:30 PM</span><span><i class="pill pill-green">Vacant</i></span><span></span><span class="badges"><b class="badge b-np">NP</b><b class="badge b-ns">NS</b></span></div>
    <div class="patient-row board-grid"><span>202</span><span>M.M.</span><span>Lorem</span><span>Lorem</span><span>1:30 PM</span><span><i class="pill pill-green">staff In Room</i></span><span><i class="alert-chip chip-emer">Staff Emer 00:35</i></span><span class="badges"><b class="badge b-fr">FR</b></span></div>
    <div class="patient-row board-grid"><span>202</span><span>M.M.</span><span>Lorem</span><span>Lorem</span><span>1:30 PM</span><span><i class="pill pill-blue">Vacant</i></span><span></span><span class="badges"><b class="badge b-pa">PA</b></span></div>
    <div class="patient-row board-grid"><span>202</span><span>M.M.</span><span>Lorem</span><span>Lorem</span><span>1:30 PM</span><span><i class="pill pill-blue">Vacant</i></span><span></span><span class="badges"></span></div>
    <div class="patient-row board-grid"><span>202</span><span>M.M.</span><span>Lorem</span><span>Lorem</span><span>1:30 PM</span><span><i class="pill pill-blue">Vacant</i></span><span></span><span class="badges"></span></div>
  </div>

  <nav class="pager" aria-label="Pages">
    <svg width="17" height="17" viewBox="0 0 17 17" aria-label="Previous page"><circle cx="8.5" cy="8.5" r="8.5" fill="#0a7cf5"/><path d="M10 5 L6.5 8.5 L10 12" fill="none" stroke="#fff" stroke-width="1.2"/></svg>
    <svg width="17" height="17" viewBox="0 0 17 17" aria-label="Next page"><circle cx="8.5" cy="8.5" r="7.9" fill="none" stroke="#666" stroke-width="0.9"/><path d="M7 5 L10.5 8.5 L7 12" fill="none" stroke="#666" stroke-width="1"/></svg>
  </nav>
</section>

</body>
</html>
```